Southern Grain Assurance- Web & Business card design for a new business within the Ag Sector

HELLO!!!!

We need your help in relation to web design (business cards and stationary if possible!) for a new company based in NSW, Australia.

The name of the business is: Southern Grain Assurance (SGA). I have quickly mocked a webpage just to give you an idea of what we are looking for.... http://fieldmockup7.sitebuildly.example/http

SGA is a strategic advisory, investment manager and problem solver within the Australian Agricultural sector.

Our Mission:

We are here to provide solutions to ALL of our Clients needs and desires within the Agricultural space.

Our Team:

Our team has worked with some of the largest & oldest Agricultural companies in Australia

We provide our Clients with a unique blend of the best Corporate as well as Operational experience that the Industry has to offer.

Client-driven Services Approach:

SGA offers a tailored service in order to meet the objectives and outcomes for each and every client.

Some of our services include:

- Food Security / Supply

- Procurement strategies within and across agricultural supply-chains

- Strategic Agribusiness advice for both Australian and Chinese based agricultural enterprises

- M&A / Due Diligence

- Corporate governance & risk management strategies.

I have attached a copy of our capability statement for background reading.

We look forward to receiving your designs!!!!!!!
Updates

Target Market(s)

Corporate, Family Offices, Food Services & Supermarkets - that are looking to obtain products within the agricultural space. Whether it be boxed beef, grain, live animals, advice - ie M&A, Due diligence - just think anything "Agricultural" and we can provide a solution

Industry/Entity Type

Agriculture

Contact Information for Business Card

See below

With respect to the business cards:

There are 2 Managing Directors:

1. Martin Pellow
Managing Director
E: martin.pellow@southerngrainassurance.example
M: +61 491 203 664
W: www.southerngrainassurance.example

2. Kate Wrenley
Managing Director
E: kate.wrenley@southerngrainassurance.example
M: +61 432 796 018

Please see attached 2 * Files named Brenmoor that outline a layout of business card that I like

Coding

Coded - Design and coding required

Number of Pages Required

5+ page

Font styles to use
Sans Serif
Other font styles liked:
• Calibri

Requirements
Must have
• I like the look of this website: http://pastoralvx.example/
• And I like the themes in the website that I have mocked up: http://fieldmockup7.sitebuildly.example/http
• The wow factor, with a professional twist.
• With respect to the website - would like it to follow the flow of the capability statement - ie with a home page, and the four additional pages:
• ABOUT US
• OUR SERVICES
• OUR TEAM
• CONTACT DETAILS
• The powerpoint presentation that I have attached is simply there for content direction - not design direction.
• As a result, am looking for web design / business card that stands out - is corporate - yet still agricultural feel.
• "capability statement" simply refers to a document that outlines our capabilities - and does not form part of the business name.
• A black angus cow, or a stalk of wheat - greens and yellows may better represent the Ag space.
• This s a draft mock-up of a web-site I created with one of those free web-page makers... This should give you a feel - crisp - whites - yet agricultural tones to highlight
• The attachments below should be used as inspiration - and don't need to be the actual shots used.

```html
<!DOCTYPE html>
<html lang="en">
<head>
<meta charset="utf-8">
<title>Southern Grain Assurance</title>
<link rel="stylesheet" href="https://fonts.googleapis.com/css2?family=PT+Sans:wght@400;700&family=PT+Serif:wght@400&display=swap">
<style>
:root{
  --page:#f1f1f1;
  --paper:#ffffff;
  --ink:#2b2b2b;
  --muted:#4a4a4a;
  --nav:#3b3b3b;
  --nav-active:#111111;
  --label:#0b0b0b;
  --accent:#c8120f;
  --blush:#f8e4e3;
  --blush-edge:#efc9c7;
  --footer:#3a3a3a;
  --footer-text:#b5b5b5;
  --line:#dcdcdc;
}
*{box-sizing:border-box;margin:0;padding:0}
html,body{width:917px;height:1200px;overflow:hidden}
body{background:var(--page);font-family:"PT Sans",Arial,sans-serif;color:var(--ink);position:relative}
.sheet{position:absolute;left:119px;top:0;width:678px;height:933px;background:var(--paper)}
.brand{position:absolute;left:165px;top:40px;display:flex;align-items:center;gap:8px;font-family:"PT Serif",Georgia,serif;font-size:21px;color:#111}
.brand-mark{width:14px;height:14px;background:#111}
.main-nav{position:absolute;left:164px;top:112px;width:588px;height:29px;background:var(--nav);display:flex}
.main-nav a{color:#fff;text-decoration:none;font-size:12px;line-height:29px;padding:0 8px;text-transform:uppercase}
.main-nav a.active{background:var(--nav-active)}
.nav-social{margin-left:auto;display:flex}
.nav-social span{width:32px;height:29px;border-left:1px solid #555;display:flex;align-items:center;justify-content:center}
.nav-social span::after{content:"";width:14px;height:14px;background:#fff}
.hero{position:absolute;left:164px;top:141px;width:588px;height:303px;background:linear-gradient(180deg,#3f5a2e 0%,#5e7f3c 30%,#2b2b25 55%,#7fa34a 80%,#9bbd5c 100%)}
.hero-title{position:absolute;left:224px;top:206px;padding:0 10px;height:32px;line-height:32px;background:rgba(0,0,0,.55);color:#fff;font-size:17px;font-weight:700}
.hero-text{position:absolute;left:224px;top:252px;width:336px;padding:6px 10px;background:rgba(0,0,0,.45);color:#fff;font-size:11.5px;line-height:15.5px}
.slide-arrow{position:absolute;top:264px;width:58px;height:58px;border-radius:50%;background:#fff;box-shadow:0 1px 4px rgba(0,0,0,.25)}
.slide-arrow svg{position:absolute;left:19px;top:15px}
.slide-arrow.prev{left:133px}
.slide-arrow.next{left:727px}
.intro{position:absolute;left:164px;top:474px;width:588px;text-align:center}
.intro h1{font-family:"PT Serif",Georgia,serif;font-weight:400;font-size:23px;color:var(--ink)}
.intro p{margin:14px auto 0;width:500px;font-size:12.5px;line-height:15px;color:var(--muted)}
.cards{position:absolute;left:165px;top:564px;display:flex;gap:10px}
.card{width:140px;height:332px;border:1px solid var(--line);background:#fff;position:relative}
.card-photo{height:144px}
.card-label{position:relative;height:25px;background:var(--label);color:#fff;font-family:"PT Serif",Georgia,serif;font-size:14.5px;text-align:center;line-height:25px}
.card-label::after{content:"";position:absolute;left:62px;bottom:-7px;border:7px solid transparent;border-bottom:0;border-top-color:var(--label)}
.card p{margin:24px 3px 0;text-align:center;font-size:10.8px;line-height:14px;color:#333}
.card .more{position:absolute;left:27px;top:278px;width:84px;height:26px;background:var(--accent);color:#fff;font-size:11px;font-weight:700;line-height:26px;text-align:center;text-decoration:none}
.photo-wheat{background:linear-gradient(135deg,#f4dfa8,#d9a447 60%,#b67a22)}
.photo-harvest{background:linear-gradient(180deg,#cfe0ea 0%,#6c6c5e 45%,#a06a3e 80%,#5aa93c)}
.photo-field{background:linear-gradient(160deg,#c7d9b4,#8ba87a 50%,#d9d0c4)}
.photo-desk{background:linear-gradient(180deg,#eef0f1,#d9c2a9 55%,#f3f3f3)}
.about-band{position:absolute;left:107px;top:933px;width:704px;height:158px;background:var(--blush);text-align:center}
.about-band::before,.about-band::after{content:"";position:absolute;top:-12px;border-bottom:12px solid var(--blush-edge)}
.about-band::before{left:0;border-left:12px solid transparent}
.about-band::after{right:0;border-right:12px solid transparent}
.about-band h2{margin-top:32px;font-family:"PT Serif",Georgia,serif;font-weight:400;font-size:21px;color:var(--ink)}
.about-band p{margin:10px auto 0;width:500px;font-size:12px;line-height:14.5px;color:var(--muted)}
.site-footer{position:absolute;left:107px;top:1091px;width:704px;height:109px;background:var(--footer);text-align:center}
.footer-social{display:flex;justify-content:center;gap:8px;margin-top:33px}
.footer-social span{width:24px;height:24px;background:#5c5c5c;display:flex;align-items:center;justify-content:center}
.footer-social span::after{content:"";width:10px;height:10px;background:#e6e6e6}
.site-footer small{display:block;margin-top:12px;font-size:10px;color:var(--footer-text)}
</style>
</head>
<body>
<div class="sheet"></div>

<div class="brand"><span class="brand-mark"></span>Southern Grain Assurance</div>

<nav class="main-nav">
  <a class="active" href="#">Home</a>
  <a href="#">About Us</a>
  <a href="#">Our Services</a>
  <a href="#">Our Team</a>
  <a href="#">Contact Detail</a>
  <div class="nav-social"><span></span><span></span><span></span></div>
</nav>

<div class="hero" role="img" aria-label="Herd of black angus cattle grazing in a green paddock"></div>
<div class="hero-title">Lorem Ipsum is simply dummy</div>
<div class="hero-text">Lorem Ipsum is simply dummy text of the printing and typesetting industry. Lorem Ipsum has been the industry's standard dummy text ever since the 1500s, when an unknown printer took a galley of type and scrambled it to make a type specimen book. It has survived not only five centuries.</div>
<div class="slide-arrow prev"><svg width="20" height="28" viewBox="0 0 20 28"><path d="M14 2 L5 14 L14 26" fill="none" stroke="#333" stroke-width="1.6"/></svg></div>
<div class="slide-arrow next"><svg width="20" height="28" viewBox="0 0 20 28"><path d="M6 2 L15 14 L6 26" fill="none" stroke="#333" stroke-width="1.6"/></svg></div>

<section class="intro">
  <h1>Lorem Ipsum is simply dummy</h1>
  <p>Contrary to popular belief, Lorem Ipsum is not simply random text. It has roots in a piece of classical Latin literature from 45 BC,.</p>
</section>

<section class="cards">
  <article class="card">
    <div class="card-photo photo-wheat" role="img" aria-label="Golden wheat ears"></div>
    <div class="card-label">About US</div>
    <p>Lorem Ipsum is simply dummy text of the printing and typesetting industry. Lorem Ipsum.Lorem Ipsum is simply</p>
    <a class="more" href="#">Read more</a>
  </article>
  <article class="card">
    <div class="card-photo photo-harvest" role="img" aria-label="Harvester machinery working a field"></div>
    <div class="card-label">OUR SERVICES</div>
    <p>Lorem Ipsum is simply dummy text of the printing and typesetting industry. Lorem Ipsum.Lorem Ipsum is simply</p>
    <a class="more" href="#">Read more</a>
  </article>
  <article class="card">
    <div class="card-photo photo-field" role="img" aria-label="Two agronomists reviewing a tablet in a field"></div>
    <div class="card-label">OUR TEAM</div>
    <p>Lorem Ipsum is simply dummy text of the printing and typesetting industry. Lorem Ipsum.Lorem Ipsum is simply</p>
    <a class="more" href="#">Read more</a>
  </article>
  <article class="card">
    <div class="card-photo photo-desk" role="img" aria-label="Customer support agent wearing a headset"></div>
    <div class="card-label">CONTACT</div>
    <p>Lorem Ipsum is simply dummy text of the printing and typesetting industry. Lorem Ipsum.Lorem Ipsum is simply</p>
    <a class="more" href="#">Read more</a>
  </article>
</section>

<section class="about-band">
  <h2>Southern Grain Assurance</h2>
  <p>Contrary to popular belief, Lorem Ipsum is not simply random text. It has roots in a piece of classical Latin literature from 45 BC, making it over 2000 years old. Harold Finchley,  looked up one of the more obscure Latin words, consectetur, from a Lorem Ipsum passage, and going through the cites of the word in classical literature,</p>
</section>

<footer class="site-footer">
  <div class="footer-social"><span></span><span></span><span></span></div>
  <small>Copyright © Southern Grain Assurance .Com 2015 – All Rights Reserved</small>
</footer>
</body>
</html>
```